Nordic Joinery Guild Wordpress Theme and newsletter template

We at the NJG are looking to start a Wordpress website and also send out a newsletter (web). We have just completed a Logo design project with ArtFlockly and we were so pleased with the results that we would like to see what the designers can come up with for a Wordpress theme and a template for an online newsletter. The theme has to support Icelandic letters. It also has to have a subscription option by email. We would need to have the option to add advertisement banners. The theme has to be easy to work with.
Below we have added a two websites for a example of what we are looking for: .
http://www.torvexhub.example/
http://www.brakkel.example/
The newsletter has to have a similar theme as the website and will be used with MS Publisher.

Attached is the new NJG logo.
Updates

Project Deadline Extended Reason: Not fully happy with the designs we have gotten so far. Would like to extend time to see if improvements can be made. Added Tuesday, June 16, 2015

Target Market(s)

Welding association members, welding and metalworking industry, suppliers in welding industry, International welding community, other national welding associations, welding education community

Industry/Entity Type

Welding

Number of Pages Required

3 page

Requirements
Must have
• The TKBÓ logo
• Icelandic letters
• email formpage
• Advertisement space/banners/buttons
• Easy to manage
• Compatible with Wordpress
Nice to have
• Welding pictures
• Nice graphics
Should not have
• Should not be dark and heavy set.

```html
<!DOCTYPE html>
<html lang="is">
<head>
<meta charset="utf-8">
<title>TKBÓ – Nordic Joinery Guild</title>
<link href="https://fonts.googleapis.com/css2?family=Open+Sans:wght@300;400;600;700&family=Oswald:wght@500;700&display=swap" rel="stylesheet">
<style>
:root{
  --red:#d8262b;
  --red-dark:#a5181c;
  --red-deep:#8e1317;
  --ink:#222;
  --text:#333;
  --muted:#888;
  --page-grey:#ececec;
  --header-grey:#eeeeee;
  --card-grey:#ededed;
  --navy:#1f4e7a;
  --dark:#232323;
  --darker:#161616;
  --field:#3d3d3d;
  --white:#fff;
}
*{box-sizing:border-box;margin:0;padding:0}
html,body{width:689px;height:1200px;overflow:hidden}
body{position:relative;background:var(--white);font-family:"Open Sans",Arial,sans-serif;color:var(--text)}
.abs{position:absolute}

/* header */
.site-header{left:0;top:0;width:689px;height:76px;background:var(--header-grey)}
.brand{left:98px;top:14px;display:flex;align-items:center;gap:6px}
.brand-dot{width:12px;height:12px;border-radius:50%;background:var(--red)}
.brand-name{font-family:"Open Sans",sans-serif;font-weight:700;font-size:30px;color:var(--red);letter-spacing:-1px;line-height:1}
.brand-sub{left:99px;top:50px;font-size:6.5px;font-weight:700;color:var(--red);letter-spacing:.2px}
.help-label{left:547px;top:24px;font-size:10px;color:var(--ink)}
.phone{left:452px;top:37px;display:flex;align-items:center;gap:6px}
.phone-num{font-family:"Oswald",sans-serif;font-weight:700;font-size:21px;color:var(--navy);line-height:1}

/* nav */
.main-nav{left:0;top:76px;width:689px;height:28px;background:linear-gradient(#e0363a,#c81f24)}
.nav-list{left:88px;top:76px;height:28px;display:flex;list-style:none}
.nav-list li{height:28px;display:flex;align-items:center;justify-content:center;font-size:8px;font-weight:700;color:var(--white);border-right:1px solid rgba(0,0,0,.15)}
.nav-list li.active{background:var(--red-deep)}
.social{left:508px;top:76px;width:92px;height:28px;background:var(--red-dark);display:flex;align-items:center;justify-content:center;gap:7px}
.social span{width:13px;height:13px;border-radius:50%;border:1px solid var(--white)}

/* hero */
.hero{left:0;top:104px;width:689px;height:291px;background:linear-gradient(100deg,#f1b55c 0%,#c77b2c 30%,#6a4a2e 55%,#4a4038 75%,#2f2a26 100%)}
.hero-caption{left:104px;top:327px;width:482px;height:44px;background:rgba(216,38,43,.9);display:flex;align-items:center;justify-content:center;font-family:"Oswald",sans-serif;font-weight:700;font-size:28px;color:var(--white);letter-spacing:.2px}
.dots{left:331px;top:379px;display:flex;gap:4px}
.dots span{width:6px;height:6px;border-radius:50%;background:var(--white)}
.dots span.off{background:#aaa}

/* welcome */
.welcome{left:0;top:395px;width:689px;height:202px;background:var(--page-grey)}
.welcome-title{left:0;top:411px;width:689px;text-align:center;font-weight:300;font-size:21px;color:var(--ink)}
.welcome-title b{font-weight:700;color:var(--red)}
.rule{left:110px;width:468px;height:1px;background:#c8c8c8}
.welcome-text{left:110px;top:450px;width:470px;text-align:center;font-size:7.6px;line-height:12.1px;color:#444}

/* news */
.news-title{left:0;top:617px;width:689px;text-align:center;font-weight:300;font-size:19px;color:var(--ink)}
.card{width:234px;height:110px;background:var(--card-grey);display:flex}
.card.featured{outline:1px solid #bbb;outline-offset:2px}
.card-photo{width:110px;height:110px;flex:none}
.card-body{padding:5px 9px;position:relative;flex:1}
.card-title{font-size:10px;font-weight:700;line-height:13px;color:var(--ink)}
.card-date{margin-top:4px;width:86px;height:12px;background:var(--white);border:1px solid #ddd;font-size:6.5px;line-height:10px;padding-left:4px;color:#999}
.card-date b{color:#666}
.card-text{margin-top:5px;font-size:7.6px;line-height:10.5px;color:#333}
.card-more{position:absolute;right:8px;bottom:6px;font-size:8px;color:var(--red)}

/* contact */
.contact{left:0;top:943px;width:689px;height:225px;background:var(--dark)}
.contact-title{left:0;top:960px;width:689px;text-align:center;font-weight:300;font-size:19px;color:var(--white)}
.label{font-size:9.5px;color:var(--white)}
.field{background:var(--field)}
.submit{left:499px;top:1112px;width:55px;height:21px;background:var(--white);border-radius:3px;font-size:9.5px;color:#000;display:flex;align-items:center;justify-content:center}

/* footer */
.site-footer{left:0;top:1168px;width:689px;height:32px;background:var(--darker);display:flex;align-items:center;justify-content:center;font-size:6.5px;color:#ddd}
.site-footer b{font-weight:700}
</style>
</head>
<body>

<header class="abs site-header"></header>
<div class="abs brand"><span class="brand-dot"></span><span class="brand-name">TKBÓ</span></div>
<div class="abs brand-sub">TIMBURKJÖR BÓLSTAÐAR</div>
<div class="abs help-label">NEED HELP</div>
<div class="abs phone">
  <svg width="21" height="21" viewBox="0 0 21 21" aria-hidden="true">
    <circle cx="10.5" cy="10.5" r="9" fill="none" stroke="#d8262b" stroke-width="2"/>
    <path d="M7 6.5c.6-.6 1.3-.5 1.6 0l1 1.6c.3.5.1 1-.3 1.3l-.5.4c.5 1.1 1.3 1.9 2.4 2.4l.4-.5c.3-.4.8-.6 1.3-.3l1.6 1c.5.3.6 1 0 1.6-.9.9-2 1-3.3.3-1.8-1-3.1-2.3-4.1-4.1C6 8.5 6.1 7.4 7 6.5z" fill="#d8262b"/>
  </svg>
  <span class="phone-num">123-456-7890</span>
</div>

<nav class="abs main-nav"></nav>
<ul class="abs nav-list">
  <li class="active" style="width:60px">HOME</li>
  <li style="width:64px">NEWS</li>
  <li style="width:81px">EDUCATION</li>
  <li style="width:70px">LIBERTY</li>
  <li style="width:57px">BLOG</li>
  <li style="width:88px">CONTACT US</li>
</ul>
<div class="abs social" aria-label="Social links"><span></span><span></span><span></span><span></span></div>

<div class="abs hero" role="img" aria-label="Photo of a worker in gloves using an angle grinder with sparks flying"></div>
<div class="abs hero-caption">COMMITMENT TO OUR CUSTOMERS</div>
<div class="abs dots"><span></span><span class="off"></span><span></span></div>

<section class="abs welcome"></section>
<h1 class="abs welcome-title">Welcome to <b>TKBÓ</b></h1>
<div class="abs rule" style="top:444px"></div>
<p class="abs welcome-text">Lorem ipsum dolor sit amet conse ctetur adipisicing elit, sed do eiusmod tempor incididunt ut labore et dolore magna aliqua. Ut enim ad minim veniam, quis nostrud exercitation ullamco laboris nisi ut aliquip ex ea commodo consequat. Duis aute irure dolor in reprehenderit in voluptate velit esse cillum dolore eu fugiat nulla pariatur. Excepteur sint occaecat cupidatat non proident, sunt in culpa qui officia deserunt mollit anim id est laborum. Lorem ipsum dolor sit amet conse ctetur adipisicing elit, sed do eiusmod tempor incididunt ut labore et dolore magna aliqua. Ut enim ad minim veniam, quis nostrud exercitation ullamco laboris nisi ut aliquip ex ea commodo conse or sit amet conse ctetur adipisicing elit, sed do eiusmod tempor incididunt ut labore et dolore magna aliqua. Ut enim ad minim veniam, quis nostrud exercitation ullamco laboris nisi ut aliquip ex ea commodo consequat. Duis aute irure dolor in reprehenderit in voluptate velit esse cillum dolore eu fugiat nulla pariatur. Excepteur sint occaecat cupidatat non proident, sunt in.</p>
<div class="abs rule" style="top:567px"></div>

<h2 class="abs news-title">Latest News</h2>

<article class="abs card" style="left:103px;top:660px">
  <div class="card-photo" role="img" aria-label="Photo of glowing hot steel in a rolling mill" style="background:linear-gradient(135deg,#8a6a5a,#d5562a 60%,#f0a050)"></div>
  <div class="card-body"><div class="card-title">Lorem ipsum dolor sit amet conse</div><div class="card-date"><b>On:</b> Jun 18, 2015</div><div class="card-text">Lorem ipsum dolor sit amet conse ctetur adipisicing elit, sed do eiusmod.</div><div class="card-more">more...</div></div>
</article>
<article class="abs card featured" style="left:353px;top:660px">
  <div class="card-photo" role="img" aria-label="Photo of a cutting torch on a steel plate" style="background:linear-gradient(135deg,#5a4a48,#8a7a78 50%,#d9c2d8)"></div>
  <div class="card-body"><div class="card-title">Lorem ipsum dolor sit amet conse</div><div class="card-date"><b>On:</b> Jun 18, 2015</div><div class="card-text">Lorem ipsum dolor sit amet conse ctetur adipisicing elit, sed do eiusmod.</div><div class="card-more">more...</div></div>
</article>
<article class="abs card" style="left:103px;top:789px">
  <div class="card-photo" role="img" aria-label="Photo of a worker cutting metal beside gas cylinders" style="background:linear-gradient(135deg,#6e6a66,#8a5a40 55%,#c99a5a)"></div>
  <div class="card-body"><div class="card-title">Lorem ipsum dolor sit amet conse</div><div class="card-date"><b>On:</b> Jun 18, 2015</div><div class="card-text">Lorem ipsum dolor sit amet conse ctetur adipisicing elit, sed do eiusmod.</div><div class="card-more">more...</div></div>
</article>
<article class="abs card" style="left:353px;top:789px">
  <div class="card-photo" role="img" aria-label="Photo of a welder in a mask with bright sparks" style="background:linear-gradient(135deg,#1e2a40,#3a4a6a 55%,#c07a40)"></div>
  <div class="card-body"><div class="card-title">Lorem ipsum dolor sit amet conse</div><div class="card-date"><b>On:</b> Jun 18, 2015</div><div class="card-text">Lorem ipsum dolor sit amet conse ctetur adipisicing elit, sed do eiusmod.</div><div class="card-more">more...</div></div>
</article>

<section class="abs contact"></section>
<h2 class="abs contact-title">Contact Us</h2>
<div class="abs label" style="left:134px;top:1006px">Name :</div>
<div class="abs field" style="left:134px;top:1021px;width:195px;height:29px"></div>
<div class="abs label" style="left:134px;top:1063px">Email :</div>
<div class="abs field" style="left:134px;top:1076px;width:195px;height:29px"></div>
<div class="abs label" style="left:360px;top:1006px">Massage :</div>
<div class="abs field" style="left:360px;top:1021px;width:195px;height:83px"></div>
<div class="abs submit">Submit</div>

<footer class="abs site-footer">© 2015 |&nbsp;<b>Timburkjör Bólstaðar</b>&nbsp;| All rights reserved | Privacy policy.</footer>

</body>
</html>
```